Norvale Investment Management Needs Door Wording Design

We need someone to put together a design for our glass front doors (2).

The words could be, but aren't limited to, as follows:

"100
Gently Restored Bodywork Studio
*Ring Bell"

and

"200 & 300
Norvale Investment Management inc.
*Ring Bell"

The design should be clean, subtle and professional. It is a simple mainly glass door with a black frame. Our website is www.norvaleinvest.ca for a more detailed description of what we do. The adjacent business would also be involved, as per the wording of the Gently Restored Bodywork Studio.

We are looking for something to bring out the wording on the door (there is currently a piece of paper printed and taped to the inside).

Dimensions of the window are 47 inches x 23 inches.

Thanks!

Colors
000000
ffffff

Requirements
Must have
• The previous words
Nice to have
• Creative flair, taking into consideration the nature of our business (Investment Management)

```html
<!DOCTYPE html>
<html lang="en">
<head>
<meta charset="utf-8">
<title>200 Door – Norvale Investment Management</title>
<link rel="stylesheet" href="https://fonts.googleapis.com/css2?family=Russo+One&family=Tinos&display=swap">
<style>
  :root {
    --backdrop: #cccbc9;
    --label-grey: #878382;
    --door-black: #000000;
    --door-white: #ffffff;
  }
  html, body {
    margin: 0;
    padding: 0;
    width: 720px;
    height: 1200px;
    overflow: hidden;
    background: var(--backdrop);
  }
  .canvas {
    position: relative;
    width: 720px;
    height: 1200px;
  }
  .door-label {
    position: absolute;
    top: 38px;
    left: 0;
    width: 690px;
    margin: 0;
    text-align: center;
    font-family: "Tinos", "Times New Roman", serif;
    font-weight: 400;
    font-size: 34px;
    letter-spacing: 0.5px;
    color: var(--label-grey);
  }
  .door-panel {
    position: absolute;
    left: 125px;
    top: 120px;
    width: 469px;
    height: 960px;
    background: var(--door-black);
    overflow: hidden;
  }
  .door-stripes {
    position: absolute;
    inset: 0;
  }
  .door-stripes line {
    stroke: var(--door-white);
    stroke-width: 22;
  }
  .brand-block {
    position: absolute;
    left: 0;
    top: 318px;
    width: 469px;
    display: flex;
    flex-direction: column;
    align-items: center;
  }
  .brand-square {
    width: 200px;
    height: 200px;
    box-sizing: border-box;
    border: 26px solid var(--door-white);
  }
  .brand-name {
    margin: 40px 0 0;
    font-family: "Russo One", "Arial Black", sans-serif;
    font-weight: 400;
    font-size: 46px;
    letter-spacing: 2px;
    line-height: 1;
    color: var(--door-white);
  }
</style>
</head>
<body>
  <main class="canvas">
    <p class="door-label">200 DOOR</p>

    <section class="door-panel" aria-label="Door 200 – Norvale Investment Management">
      <svg class="door-stripes" width="469" height="960" viewBox="0 0 469 960" aria-hidden="true">
        <line x1="180" y1="-34" x2="520" y2="239"/>
        <line x1="260" y1="-36" x2="520" y2="172"/>
        <line x1="-40" y1="708" x2="320" y2="996"/>
        <line x1="-40" y1="775" x2="240" y2="999"/>
      </svg>

      <div class="brand-block">
        <div class="brand-square" aria-hidden="true"></div>
        <p class="brand-name">NORVALE</p>
      </div>
    </section>
  </main>
</body>
</html>
```